Business card design needed

I need a business card design for a dog walking, dog minding and dog training business. Please refer to my website for the basic company colours and fonts I'm after. Planning on a double sided card, so all information doesn't need to be on the 'front' side.
Cheers

Industry/Entity Type

Dog Training

Contact Information for Business Card

Meadow Paws - happy hounds
Rua 0498307164
meadowpawsdemo.com.au
-walking
-holiday stays
-onsite care
-training and behavioural consultations

```html
<!DOCTYPE html>
<html lang="en">
<head>
<meta charset="utf-8">
<title>Meadow Paws – business card</title>
<link rel="stylesheet" href="https://fonts.googleapis.com/css2?family=Exo+2:wght@300;400;600;700&display=swap">
<style>
  :root {
    --backdrop: #e9e6e1;
    --charcoal: #3b3c41;
    --charcoal-deep: #2f3034;
    --orange: #ea6a1c;
    --orange-deep: #d9431a;
    --ink-light: #f1efec;
    --ink-soft: #d9d7d4;
    --ink-dark: #3d4048;
    --card-shadow: rgba(40, 30, 20, 0.28);
  }
  * { box-sizing: border-box; margin: 0; padding: 0; }
  html, body {
    width: 1200px;
    height: 720px;
    overflow: hidden;
    background: var(--backdrop);
    font-family: "Exo 2", "Segoe UI", sans-serif;
  }
  .canvas {
    width: 1200px;
    height: 720px;
    display: flex;
    align-items: center;
    justify-content: center;
    gap: 56px;
  }
  .card {
    position: relative;
    width: 504px;
    height: 288px;
    border-radius: 3px;
    box-shadow: 0 14px 30px var(--card-shadow);
    overflow: hidden;
  }
  .card--front {
    background: linear-gradient(160deg, var(--charcoal) 0%, var(--charcoal-deep) 100%);
    color: var(--ink-light);
  }
  .card--back {
    background: linear-gradient(150deg, var(--orange) 0%, var(--orange-deep) 100%);
    color: var(--ink-light);
  }

  /* front: contact block */
  .contact {
    position: absolute;
    top: 26px;
    right: 28px;
    text-align: right;
  }
  .contact__line {
    font-size: 22px;
    font-weight: 300;
    letter-spacing: 0.5px;
  }
  .contact__name { font-weight: 700; }
  .contact__area {
    margin-top: 4px;
    font-size: 13px;
    font-weight: 300;
    color: var(--ink-soft);
    letter-spacing: 0.3px;
  }

  /* shared brand block */
  .brand {
    position: absolute;
    display: flex;
    align-items: center;
    gap: 18px;
  }
  .brand__portrait {
    width: 104px;
    height: 150px;
    border-radius: 4px;
  }
  .card--front .brand { left: 26px; bottom: 28px; }
  .card--front .brand__portrait {
    background: linear-gradient(180deg, rgba(255,255,255,0.16), rgba(255,255,255,0.06));
  }
  .card--back .brand { left: 30px; bottom: 34px; }
  .card--back .brand__portrait {
    background: linear-gradient(180deg, rgba(255,255,255,0.22), rgba(255,255,255,0.08));
  }
  .brand__words { display: flex; flex-direction: column; }
  .brand__name {
    display: flex;
    align-items: center;
    gap: 10px;
    font-size: 40px;
    font-weight: 400;
    letter-spacing: 1.5px;
    text-transform: uppercase;
    line-height: 1;
  }
  .brand__dot {
    width: 12px;
    height: 12px;
    border-radius: 50%;
    flex: none;
  }
  .card--front .brand__name { color: var(--ink-light); }
  .card--front .brand__dot { background: var(--orange); }
  .card--back .brand__name { color: var(--ink-light); }
  .card--back .brand__dot { background: var(--ink-dark); }
  .brand__tagline {
    margin-top: 6px;
    padding-left: 22px;
    font-size: 20px;
    font-weight: 300;
    letter-spacing: 0.4px;
  }
  .card--front .brand__tagline { color: var(--ink-soft); }
  .card--back .brand__tagline { color: var(--ink-light); }

  /* back: mission statement */
  .mission {
    position: absolute;
    top: 24px;
    right: 26px;
    width: 250px;
    text-align: right;
    font-size: 13px;
    font-weight: 300;
    line-height: 1.4;
    color: var(--ink-light);
  }
  .mission strong { font-weight: 700; }
</style>
</head>
<body>
  <main class="canvas">
    <section class="card card--front" aria-label="Card front">
      <div class="contact">
        <p class="contact__line"><span class="contact__name">Rua</span> 0498 307 164</p>
        <p class="contact__area">servicing the inner suburbs of Melbourne</p>
      </div>
      <div class="brand">
        <div class="brand__portrait" role="img" aria-label="Outline illustration of a standing dog on a lead"></div>
        <div class="brand__words">
          <p class="brand__name"><span class="brand__dot"></span>Meadow Paws</p>
          <p class="brand__tagline">happy hounds</p>
        </div>
      </div>
    </section>

    <section class="card card--back" aria-label="Card back">
      <p class="mission">We're about a <strong>good balance</strong> of <strong>fun, exercise, proper stimulation</strong> and <strong>reinforcing good habits</strong> and <strong>canine manners</strong></p>
      <div class="brand">
        <div class="brand__portrait" role="img" aria-label="Outline illustration of a standing dog with a collar"></div>
        <div class="brand__words">
          <p class="brand__name"><span class="brand__dot"></span>Meadow Paws</p>
          <p class="brand__tagline">happy hounds</p>
        </div>
      </div>
    </section>
  </main>
</body>
</html>
```